Mission statement design for a secondary school

We have the content of our mission statement and need an appealing layout. The design should fit on a poster or A4 page. The content grouping in the document should also be graphically recognizable. Our target group are young people and their parents as well as the school staff, which is why we need a modern design that is not out after 2 years. It must be easy to grasp visually and graphically simple.

Target Market(s)

Actors of the school

Requirements
Must have
• cantonal logo including school name see document can be integrated as a header
Should not have
• References to trademarks or third parties

```html
<!DOCTYPE html>
<html lang="de">
<head>
<meta charset="utf-8">
<title>Unser Leitbild – Sekundarschule Talheim</title>
<link rel="stylesheet" href="https://fonts.googleapis.com/css2?family=Poppins:wght@300;700;800&family=Roboto:wght@400&family=Space+Mono:wght@700&display=swap">
<style>
  :root {
    --red: #e52d35;
    --grey-dark: #616163;
    --grey-text: #4a4a4c;
    --grey-icon: #a9a9ab;
    --header-bg: #fafafa;
    --body-bg-top: #f1f1f3;
    --body-bg-bottom: #ececee;
    --stage: #3a3a3a;
  }
  * { margin: 0; padding: 0; box-sizing: border-box; }
  html, body { width: 1180px; height: 1200px; overflow: hidden; }
  body { background: var(--stage); position: relative; font-family: "Roboto", Arial, sans-serif; }

  .poster {
    position: absolute; left: 182px; top: 20px;
    width: 816px; height: 1160px;
    background: linear-gradient(var(--body-bg-top), var(--body-bg-bottom));
    overflow: hidden;
  }
  .poster > * { position: absolute; }

  .header { left: 0; top: 0; width: 816px; height: 155px; background: var(--header-bg); }
  .title {
    left: 64px; top: 40px; font-family: "Poppins", sans-serif; font-weight: 700;
    font-size: 58px; line-height: 1; color: var(--red); letter-spacing: -0.5px;
  }
  .subtitle { left: 64px; top: 100px; font-size: 24px; color: var(--grey-text); line-height: 1; }
  .authority-name {
    right: 84px; top: 52px; font-family: "Poppins", sans-serif; font-weight: 700;
    font-size: 19px; color: var(--red); line-height: 1; letter-spacing: 1px; text-transform: uppercase;
  }
  .authority-line {
    right: 84px; font-family: "Space Mono", monospace; font-weight: 700;
    font-size: 10px; color: var(--red); line-height: 1; text-align: right; letter-spacing: 0.3px;
  }
  .authority-line.dept { top: 103px; }
  .authority-line.school { top: 117px; }

  .list { list-style: none; font-size: 12px; color: var(--grey-text); line-height: 17px; }
  .list li { position: absolute; left: 0; white-space: nowrap; }
  .list li svg { position: absolute; left: -22px; top: 2px; width: 13px; height: 13px; }
  .list--red li svg { color: var(--red); }
  .list--grey li svg { color: var(--grey-dark); }

  .list.attitude { left: 96px; top: 195px; }
  .list.learning { left: 525px; top: 195px; }
  .list.development { left: 97px; top: 923px; }
  .list.community { left: 470px; top: 912px; }

  .arrows { width: 22px; }
  .arrows--red-up { left: 73px; top: 336px; color: var(--red); }
  .arrows--grey-up { left: 715px; top: 474px; color: var(--grey-dark); }
  .arrows--red-down { left: 69px; top: 840px; color: var(--red); }

  .icon { color: var(--grey-icon); }
  .icon--house { left: 122px; top: 332px; width: 52px; height: 60px; }
  .icon--book { left: 421px; top: 306px; width: 62px; height: 44px; }
  .icon--notepad { left: 110px; top: 834px; width: 50px; height: 64px; }
  .person-placeholder {
    left: 682px; top: 982px; width: 62px; height: 74px;
    background: radial-gradient(circle at 50% 40%, #cfcfd1, #dedee0 70%);
    border-radius: 30px;
  }

  .section-heading {
    left: 70px; top: 418px; font-family: "Poppins", sans-serif; font-weight: 700;
    font-size: 44px; line-height: 50px; color: var(--red); letter-spacing: -0.3px;
  }
  .keyword-main {
    left: 64px; top: 506px; font-family: "Poppins", sans-serif; font-weight: 700;
    font-size: 200px; line-height: 1; color: var(--grey-dark); letter-spacing: -5px;
  }
  .keyword-sub {
    left: 66px; top: 677px; font-family: "Poppins", sans-serif; font-weight: 300;
    font-size: 117px; line-height: 1; color: var(--red); letter-spacing: -1px;
  }
  .keyword-community {
    right: 76px; top: 845px; font-family: "Poppins", sans-serif; font-weight: 800;
    font-size: 40px; line-height: 1; color: var(--grey-dark);
  }
  .footer-band { left: 0; bottom: 2px; width: 816px; height: 10px; background: var(--red); }
</style>
</head>
<body>
<svg width="0" height="0" style="position:absolute">
  <defs>
    <symbol id="tick-box" viewBox="0 0 14 14">
      <rect x="0.8" y="0.8" width="12.4" height="12.4" rx="3" fill="none" stroke="currentColor" stroke-width="1.4"/>
      <path d="M4 7.2 L6.2 9.3 L10 4.9" fill="none" stroke="currentColor" stroke-width="1.4" stroke-linecap="round" stroke-linejoin="round"/>
    </symbol>
    <symbol id="triangles-up" viewBox="0 0 22 54">
      <path d="M11 0 L22 14 H0 Z M11 20 L22 34 H0 Z M11 40 L22 54 H0 Z" fill="currentColor"/>
    </symbol>
    <symbol id="triangles-down" viewBox="0 0 22 54">
      <path d="M0 0 H22 L11 14 Z M0 20 H22 L11 34 Z M0 40 H22 L11 54 Z" fill="currentColor"/>
    </symbol>
  </defs>
</svg>

<main class="poster">
  <header class="header"></header>
  <h1 class="title">Unser Leitbild</h1>
  <p class="subtitle">Sekundarschule Talheim</p>
  <p class="authority-name">Kanton Nordtal</p>
  <p class="authority-line dept">BILDUNGS-, KULTUR- UND SPORTDIREKTION</p>
  <p class="authority-line school">SEKUNDARSCHULE TALHEIM</p>

  <ul class="list list--red attitude">
    <li style="top:0"><svg><use href="#tick-box"/></svg>… stehen die Lernenden im Mittelpunkt.</li>
    <li style="top:30px"><svg><use href="#tick-box"/></svg>… ist Integration selbstverständlich.</li>
    <li style="top:59px"><svg><use href="#tick-box"/></svg>… begegnen wir uns respektvoll und wertschätzend.</li>
    <li style="top:86px"><svg><use href="#tick-box"/></svg>… setzen wir uns für lebenslanges Lernen ein.</li>
  </ul>

  <svg class="arrows arrows--red-up" height="54"><use href="#triangles-up"/></svg>
  <svg class="icon icon--house" viewBox="0 0 52 60" fill="none" stroke="currentColor" stroke-width="2.4" stroke-linejoin="round">
    <path d="M2 24 L26 2 L50 24 V58 H2 Z"/>
    <path d="M8 22 L26 6 L44 22"/>
    <rect x="10" y="32" width="14" height="12"/>
    <path d="M30 58 V32 H42 V58"/>
    <path d="M34 44 V48"/>
  </svg>
  <svg class="icon icon--book" viewBox="0 0 62 44" fill="none" stroke="currentColor" stroke-width="2.4" stroke-linejoin="round">
    <path d="M6 6 V36 H28 L31 39 L34 36 H56 V6"/>
    <path d="M31 10 C24 4 16 4 10 6 V32 C16 30 24 30 31 36 C38 30 46 30 52 32 V6 C46 4 38 4 31 10 Z"/>
    <path d="M31 10 V36"/>
    <path d="M2 10 V42 H60 V10"/>
  </svg>

  <h2 class="section-heading">Haltung An<br>unserer Schule...</h2>

  <ul class="list list--grey learning">
    <li style="top:0"><svg><use href="#tick-box"/></svg>Wir begleiten unsere Lernenden hin<br>zur Selbständigkeit.</li>
    <li style="top:47px"><svg><use href="#tick-box"/></svg>Wir unterstützen unsere Lernenden in<br>ihrem individuellen Kompetenzerwerb.</li>
    <li style="top:94px"><svg><use href="#tick-box"/></svg>Wir ermöglichen allen Lernenden Erfolge.</li>
    <li style="top:124px"><svg><use href="#tick-box"/></svg>Die Unterrichtsinhalte orientieren sich<br>an aktuellen Themen.</li>
    <li style="top:168px"><svg><use href="#tick-box"/></svg>Wir beurteilen transparent.</li>
    <li style="top:198px"><svg><use href="#tick-box"/></svg>Wir begegnen Heterogenität mit<br>multiprofessionellen Teams.</li>
    <li style="top:245px"><svg><use href="#tick-box"/></svg>Wir schaffen eine wertschätzende<br>und förderliche Atmosphäre.</li>
    <li style="top:292px"><svg><use href="#tick-box"/></svg>Unsere Schule bietet eine<br>zeitgemässe Infrastruktur.</li>
  </ul>
  <svg class="arrows arrows--grey-up" height="54"><use href="#triangles-up"/></svg>

  <p class="keyword-main">Lernen</p>
  <p class="keyword-sub">Entwicklung</p>

  <svg class="arrows arrows--red-down" height="54"><use href="#triangles-down"/></svg>
  <svg class="icon icon--notepad" viewBox="0 0 50 64" fill="none" stroke="currentColor" stroke-width="2.4" stroke-linecap="round">
    <rect x="2" y="6" width="46" height="56" rx="2"/>
    <path d="M2 14 H48"/>
    <path d="M8 2 V9 M13 2 V9 M18 2 V9 M23 2 V9 M28 2 V9 M33 2 V9 M38 2 V9 M43 2 V9"/>
    <path d="M10 26 H16 M22 26 H40 M10 34 H16 M22 34 H40 M10 42 H16 M22 42 H40 M10 50 H16 M22 50 H40"/>
  </svg>

  <ul class="list list--red development">
    <li style="top:0"><svg><use href="#tick-box"/></svg>Unsere Schule achtet die Gesundheit aller.</li>
    <li style="top:30px"><svg><use href="#tick-box"/></svg>Wir legen Wert auf eine offene Kommunikation.</li>
    <li style="top:60px"><svg><use href="#tick-box"/></svg>Unsere pädagogische Zusammenarbeit basiert<br>auf einer professionellen Haltung.</li>
    <li style="top:108px"><svg><use href="#tick-box"/></svg>Die Eltern sind ein Teil unserer<br>Schulgemeinschaft und tragen Verantwortung.</li>
    <li style="top:155px"><svg><use href="#tick-box"/></svg>Wir haben an unserer Schule Freiräume<br>innerhalb klarer Rahmenbedingungen.</li>
  </ul>

  <h2 class="keyword-community">Gemeinschaft</h2>

  <ul class="list list--grey community">
    <li style="top:0"><svg><use href="#tick-box"/></svg>Wir entwickeln unsere Schule gemeinsam.</li>
    <li style="top:31px"><svg><use href="#tick-box"/></svg>Wir setzen unsere Fähigkeiten und Kräfte gezielt ein.</li>
    <li style="top:61px"><svg><use href="#tick-box"/></svg>Alle tragen Verantwortung.</li>
    <li style="top:91px"><svg><use href="#tick-box"/></svg>Wir lernen alle voneinander.</li>
    <li style="top:121px"><svg><use href="#tick-box"/></svg>Wir bilden uns kontinuierlich weiter.</li>
    <li style="top:151px"><svg><use href="#tick-box"/></svg>Wir reflektieren unser Handeln.</li>
    <li style="top:182px"><svg><use href="#tick-box"/></svg>Wir sind innovativ und gehen mutig unseren Weg.</li>
  </ul>
  <div class="person-placeholder" role="img" aria-label="Outline icon of a person representing the school community"></div>

  <div class="footer-band"></div>
</main>
</body>
</html>
```